Health care product retail website

We need a website design for a company based in New Zealand that sells fresh air to an overseas market.
There are 4 products to start with and we have a logo. We need to give the message that it is unpolluted and clean. We are also promoting a self-sustaining business model by investing in the planet's future. The website will be developed in WordPress and if you can suggest coding thats a bonus, but not necessary as I can develop in Wordpress.

Target Market(s)

Chinese, Indian, Middle Eastern or anywhere where the air is quite polluted. middle-income target market

Industry/Entity Type

Health And Wellness

Number of Pages Required

5+ page

Font styles to use
Sans Serif

Requirements
Must have
• Homepage: Clean, fresh look. Indicate that the product is sourced and bottled in a clean environment.
• Any help with e-commerce and multilingual pages appreciated.
• Home, Products, Our locations, Environmental protection, Science

```html
<!DOCTYPE html>
<html lang="en">
<head>
<meta charset="utf-8">
<title>Tarn Air – Fresh Air from New Zealand</title>
<link href="https://fonts.googleapis.com/css2?family=Roboto:wght@400;500;700&family=Open+Sans:wght@400;600&display=swap" rel="stylesheet">
<style>
:root{
  --green:#7eaa10;
  --green-dark:#689010;
  --teal:#217a80;
  --price:#e0551b;
  --text:#444;
  --footer:#86b00f;
  --footer-bar:#73990b;
  --white:#fff;
}
*{margin:0;padding:0;box-sizing:border-box}
html,body{width:1200px;height:2281px;overflow:hidden;background:var(--white)}
body{position:relative;font-family:"Open Sans",Arial,sans-serif;color:var(--text)}
.abs{position:absolute}
a{color:inherit;text-decoration:none}

/* header */
.site-header{position:absolute;left:0;top:0;width:1200px;height:113px;background:var(--white)}
.brand{position:absolute;left:99px;top:34px;display:flex;align-items:center;gap:10px;font-family:"Roboto",Arial,sans-serif;font-weight:700;font-size:36px;color:var(--green)}
.brand-dot{width:26px;height:26px;border-radius:50%;background:var(--teal)}
.top-links{position:absolute;top:22px;left:0;width:1200px;height:30px;font-size:12px;color:#333}
.top-links > span{position:absolute;top:8px;white-space:nowrap}
.icon-circle{position:absolute;width:30px;height:30px;border-radius:50%;background:var(--teal);top:0}
.icon-circle svg{position:absolute;left:8px;top:8px}
.phone-num{color:var(--teal)}
.main-nav{position:absolute;top:78px;left:0;width:1200px;font-family:"Roboto",Arial,sans-serif;font-weight:700;font-size:12px;color:#333}
.main-nav a{position:absolute;white-space:nowrap}

/* hero */
.hero{position:absolute;left:0;top:113px;width:1200px;height:511px;background:linear-gradient(180deg,#3e5560 0%,#2c3f3a 40%,#1d2a1c 75%,#202a1a 100%)}
.hero-title{position:absolute;left:0;width:1200px;top:226px;text-align:center;font-family:"Roboto",Arial,sans-serif;font-weight:500;font-size:56px;color:var(--white);letter-spacing:.5px}
.hero-title .accent{color:#8cbf14}
.hero-sub{position:absolute;left:0;width:1200px;top:302px;text-align:center;font-family:"Roboto",Arial,sans-serif;font-size:27px;color:var(--white)}
.btn{position:absolute;display:flex;align-items:center;justify-content:center;background:linear-gradient(180deg,#84b31a,#6c9612);color:var(--white);font-family:"Roboto",Arial,sans-serif;font-weight:700;font-size:14px;border-radius:2px;box-shadow:0 2px 0 rgba(0,0,0,.15);white-space:nowrap}
.dots{position:absolute;display:flex;gap:6px}
.dots i{width:8px;height:8px;border-radius:50%;background:#2f3d33}
.dots i.on{background:#8cbf14}

/* sections */
.section-title{position:absolute;left:0;width:1200px;text-align:center;font-family:"Roboto",Arial,sans-serif;font-weight:700;color:var(--teal)}
.body-copy{font-size:12.5px;line-height:26px;color:var(--text)}

/* products */
.product-photo{position:absolute;width:56px;height:192px;border-radius:18px 18px 10px 10px}
.product-name{position:absolute;width:200px;text-align:center;font-family:"Roboto",Arial,sans-serif;font-weight:500;font-size:14px;line-height:20px;color:var(--teal)}
.price{position:absolute;font-family:"Roboto",Arial,sans-serif;font-weight:700;font-size:18px;color:var(--price)}
.buy{width:99px;height:32px;font-size:12px}

/* offer band */
.offer{position:absolute;left:99px;top:1434px;width:1002px;height:101px;background:var(--teal)}
.offer-label{position:absolute;left:35px;top:34px;font-family:"Roboto",Arial,sans-serif;font-weight:700;font-size:26px;line-height:30px;color:var(--white)}
.offer-text{position:absolute;left:166px;top:39px;font-size:16px;line-height:24px;color:var(--white);white-space:nowrap}

/* about */
.about-photo{position:absolute;left:99px;top:1597px;width:418px;height:269px;background:linear-gradient(160deg,#1c2a12 0%,#4f6b2a 45%,#a9b88a 70%,#2b3a1a 100%)}
.about-title{position:absolute;left:583px;top:1598px;font-family:"Roboto",Arial,sans-serif;font-weight:700;font-size:21px;color:var(--teal)}
.about-copy{position:absolute;left:583px;top:1637px;width:470px;font-size:12px;line-height:25.5px}

/* footer */
.site-footer{position:absolute;left:0;top:1933px;width:1200px;height:288px;background:var(--footer);color:var(--white)}
.footer-col{position:absolute;top:40px}
.footer-col h4{font-family:"Roboto",Arial,sans-serif;font-weight:700;font-size:13px;margin-bottom:12px}
.footer-col li{list-style:none;font-size:11.5px;line-height:27.4px}
.contact-line{font-size:11.5px;line-height:22px;display:flex;align-items:center;gap:8px}
.footer-brand{position:absolute;left:928px;top:215px;font-family:"Roboto",Arial,sans-serif;font-weight:700;font-size:26px;color:var(--white)}
.footer-bar{position:absolute;left:0;top:2221px;width:1200px;height:60px;background:var(--footer-bar);color:var(--white);font-size:11px}
.social{position:absolute;left:952px;top:25px;display:flex;gap:22px}
.social i{width:10px;height:10px;border-radius:50%;background:var(--white);display:block}
</style>
</head>
<body>

<header class="site-header">
  <div class="brand"><span class="brand-dot"></span>Tarn Air</div>
  <div class="top-links">
    <div class="icon-circle" style="left:395px">
      <svg width="14" height="14" viewBox="0 0 24 24"><path fill="#fff" d="M6.6 10.8a15 15 0 0 0 6.6 6.6l2.2-2.2c.3-.3.7-.4 1-.2 1.1.4 2.3.6 3.6.6.6 0 1 .4 1 1V20c0 .6-.4 1-1 1A17 17 0 0 1 3 4c0-.6.4-1 1-1h3.5c.6 0 1 .4 1 1 0 1.3.2 2.5.6 3.6.1.3 0 .7-.2 1z"/></svg>
    </div>
    <span style="left:436px">Call us : <span class="phone-num">(0400) 118 204</span></span>
    <span style="left:595px">My Account</span>
    <span style="left:708px">My Cart</span>
    <span style="left:800px">Login</span>
    <span style="left:880px">Register</span>
    <div class="icon-circle" style="left:953px">
      <svg width="14" height="14" viewBox="0 0 24 24"><path fill="#fff" d="M7 18a2 2 0 1 0 0 4 2 2 0 0 0 0-4zm10 0a2 2 0 1 0 0 4 2 2 0 0 0 0-4zM5.2 4H2V2h4.5l.9 2H22l-3.5 8H8.1l-.9 2H19v2H4l2.4-4.5z"/></svg>
    </div>
    <span style="left:995px">Your cart is : 0 items</span>
  </div>
  <nav class="main-nav">
    <a style="left:435px">HOME</a>
    <a style="left:532px">PRODUCTS</a>
    <a style="left:657px">OUR LOCATIONS</a>
    <a style="left:812px">ENVIRONMENTAL PROTECTION</a>
    <a style="left:1050px">SCIENCE</a>
  </nav>
</header>

<section class="hero" role="img" aria-label="Photo of a forested New Zealand coastline with islands in a calm bay">
  <h1 class="hero-title"><span class="accent">TARN</span> AIR</h1>
  <p class="hero-sub">NEW ZEALAND THAT SELLS FRESH AIR TO OVERSEAS MARKET.</p>
  <a class="btn" style="left:514px;top:357px;width:173px;height:46px">VIEW PRODUCTS</a>
  <div class="dots" style="left:576px;top:478px"><i class="on"></i><i></i><i></i></div>
</section>

<section class="welcome">
  <h2 class="section-title" style="top:680px;font-size:28px">WELCOME TO TARN AIR</h2>
  <p class="body-copy abs" style="left:134px;top:728px;width:932px;text-align:center">Lorem Ipsum is simply dummy text of the printing and typesetting industry. Lorem Ipsum has been the industry's standard dummy text ever since the 1500s, when an unknown printer took a galley of type and scrambled it to make a type specimen book. It has survived not only five centuries, but also the leap into electronic typesetting, remaining essentially unchanged. It was popularised in the 1960s with the release of Letraset sheets containing</p>
  <a class="btn" style="left:525px;top:830px;width:150px;height:43px">CONTACT HERE!</a>
</section>

<section class="featured">
  <h2 class="section-title" style="top:944px;font-size:21px">FEATURED PRODUCTS</h2>
  <p class="body-copy abs" style="left:0;top:983px;width:1200px;text-align:center">Lorem Ipsum is simply dummy text of the printing and typesetting industry has been the industry's standard dummy</p>

  <div class="product-photo" style="left:179px;top:1020px;background:linear-gradient(90deg,#5e9d10,#9ad630,#5e9d10)" role="img" aria-label="Green aluminium air bottle"></div>
  <div class="product-photo" style="left:436px;top:1020px;background:linear-gradient(90deg,#8c8c8c,#e2e2e2,#8c8c8c)" role="img" aria-label="Silver aluminium air bottle"></div>
  <div class="product-photo" style="left:697px;top:1020px;background:linear-gradient(90deg,#123f8c,#3a7ad8,#123f8c)" role="img" aria-label="Blue aluminium air bottle"></div>
  <div class="product-photo" style="left:964px;top:1020px;background:linear-gradient(90deg,#c8769a,#f3b3cf,#c8769a)" role="img" aria-label="Pink aluminium air bottle"></div>

  <p class="product-name" style="left:107px;top:1235px">Lorem Ipsum is simply<br>dummy</p>
  <p class="product-name" style="left:364px;top:1235px">Lorem Ipsum is simply<br>dummy</p>
  <p class="product-name" style="left:625px;top:1235px">Lorem Ipsum is simply<br>dummy</p>
  <p class="product-name" style="left:892px;top:1235px">Lorem Ipsum is simply<br>dummy</p>

  <span class="price" style="left:120px;top:1298px">$79.99</span>
  <a class="btn buy" style="left:196px;top:1294px">BUY NOW</a>
  <span class="price" style="left:377px;top:1298px">$79.99</span>
  <a class="btn buy" style="left:453px;top:1294px">BUY NOW</a>
  <span class="price" style="left:638px;top:1298px">$79.99</span>
  <a class="btn buy" style="left:715px;top:1294px">BUY NOW</a>
  <span class="price" style="left:904px;top:1298px">$79.99</span>
  <a class="btn buy" style="left:980px;top:1294px">BUY NOW</a>

  <div class="dots" style="left:577px;top:1366px;gap:5px"><i style="background:var(--teal)"></i><i style="background:#9cc43a"></i><i style="background:#9cc43a"></i><i style="background:#9cc43a"></i></div>
</section>

<section class="offer">
  <span class="offer-label">WE OFFER</span>
  <span class="offer-text">Lorem Ipsum is simply dummy text of the printing and typesetting industry.</span>
  <a class="btn" style="left:779px;top:31px;width:185px;height:42px">SUBSCRIBE HERE!</a>
</section>

<section class="about">
  <div class="about-photo" role="img" aria-label="Looking up at tall mossy tree trunks in a rainforest canopy"></div>
  <h2 class="about-title">ABOUT TARN AIR</h2>
  <p class="about-copy body-copy">Lorem Ipsum is simply dummy text of the printing and typesetting industry. Lorem Ipsum has been the industry's standard dummy text ever since the 1500s, when an unknown printer took a galley of type and scrambled it to make a type specimen book. It has survived not only five centuries, but also the leap into electronic typesetting, remaining essentially unchanged. It was popularised in the 1960s with the release of Letraset sheets containing...</p>
  <a class="btn" style="left:586px;top:1815px;width:162px;height:45px">VIEW MORE INFO</a>
</section>

<footer class="site-footer">
  <div class="footer-col" style="left:123px">
    <h4>CUSTOMER SERVICE</h4>
    <ul><li>About Us</li><li>Contact Us</li><li>Customer Service</li><li>Privacy Policy</li><li>Orders and Returns</li><li>Shipping Information</li><li>Our Staff Members</li></ul>
  </div>
  <div class="footer-col" style="left:380px">
    <h4>OTHERS</h4>
    <ul><li>Site Map</li><li>Advanced Search</li><li>Testimonials</li><li>Sponsorship Program</li><li>Retailer/Wholesaler Application</li><li>Our Business Partners</li><li>FAQ</li></ul>
  </div>
  <div class="footer-col" style="left:663px">
    <h4>INFORMATION</h4>
    <ul><li>Terms &amp; Conditions</li><li>Privacy policy</li><li>Disclaimer</li><li>Contact us</li><li>Sitemap</li></ul>
  </div>
  <div class="footer-col" style="left:896px">
    <h4>CONTACT INFO</h4>
    <p class="contact-line">48 Harbour Lane, Nelson,</p>
    <p class="contact-line">Postcode : 7010</p>
    <p class="contact-line" style="margin-top:6px">
      <svg width="12" height="12" viewBox="0 0 24 24"><path fill="#fff" d="M6.6 10.8a15 15 0 0 0 6.6 6.6l2.2-2.2c.3-.3.7-.4 1-.2 1.1.4 2.3.6 3.6.6.6 0 1 .4 1 1V20c0 .6-.4 1-1 1A17 17 0 0 1 3 4c0-.6.4-1 1-1h3.5c.6 0 1 .4 1 1 0 1.3.2 2.5.6 3.6.1.3 0 .7-.2 1z"/></svg>
      (0400) 118 205</p>
    <p class="contact-line" style="margin-top:5px">
      <svg width="12" height="10" viewBox="0 0 24 18"><path fill="#fff" d="M0 0h24v2L12 10 0 2zM0 4.5l12 8 12-8V18H0z"/></svg>
      hello@tarnair.example</p>
  </div>
  <div class="footer-brand">Tarn Air</div>
</footer>

<div class="footer-bar">
  <span class="abs" style="left:114px;top:22px">© 2016, Tarn Air. All rights reserved</span>
  <span class="abs" style="left:776px;top:22px;white-space:nowrap">Connect with our social network :</span>
  <div class="social" aria-label="Social network links"><i></i><i></i><i></i><i></i><i></i></div>
</div>

</body>
</html>
```